Brightline Tech Partners Website Design

I have here a website mockup. If you need anything further please feel free to reach out to me! Thank you!

Current site: http://brightlinetechpartners.example/

We want it clean, concise and eye catching.

Menu: I want the same idea we used from pellaroweb.example with the logo in the middle and in the menu:

Home, About Us, How Can We Help?, Media, Blog, Contact Us.

Let's have the Social Media icons at the very top please.

For the banner - we want a imagevault chess image sort of like imagevault photo 122579353 or 77865526

I want the words "Plan Ahead, Work Smarter, Stay Strong" to come in one at a time and then "Brightline Tech Partners" to show up on the banner.

Maybe have "Grow Your Business with Managed IT Services from Brightline Tech Partners" somewhere permanently on the banner that still suits everything.

Services Section: Maybe we can have them as chess pieces with something along the lines of "Make Your Next Move" - Managed IT Services, New Jersey Cloud Computing, Protect Your Business Data, Managed Email Solutions (Background 514558306)

Next Area: What sets us apart?/Testimonials (I want this as a split area) (Can we please use the banner image paralex here?)

(This is for the What Sets Us Apart side)
Outsmart threats before they reach your networks.

Outperform with the newest and latest technologies to not only keep you up and running, but to keep you at an advantage.

Outlast by embracing Business Continuity with Brightline Tech Partners by your side. (I will let you choose the background for here!)

Next Area: Book Your Free Two-Hour Review! (I want a form similar to the one on the old site.)

Next area: Blogs/Sign Up for our newsletter! (Again, please choose a relevant background)

Next Area:Contact Us area with service pages. I really like the contact us part in dorvaly.example where it shows the geographical area.

Target Market(s)

Business Owners in New Jersey looking to outsource their business IT, computer and network support.

Industry/Entity Type

Information Technology

Number of Pages Required

1 page

Font styles to use
Sans Serif

Requirements
Must have
• We want this website to be very sharp. I like bright colors, creative imagery.
• In the footer I must have @ 2016 Brightline Tech Partners | Privacy Policy | Sitemap
Should not have
• I am not a fan of stuffing everything in and making it very busy. I would like clean and professional

```html
<!DOCTYPE html>
<html lang="en">
<head>
<meta charset="utf-8">
<title>Brightline Tech Partners – New Jersey IT Support</title>
<link href="https://fonts.googleapis.com/css2?family=Catamaran:wght@400;500;600;700&family=Open+Sans:wght@400;600;700&display=swap" rel="stylesheet">
<style>
:root{
  --blue:#2b76b0;
  --blue-top:#2a6fa8;
  --sky:#4f9bd4;
  --pill:#2f6e9e;
  --dark:#3a3f48;
  --hero-a:#5d6470;
  --hero-b:#2d323b;
  --ink:#222831;
  --text:#4a4f57;
  --light:#f2f2f2;
  --ring:#e4e4e4;
  --white:#ffffff;
  --head:"Catamaran",sans-serif;
  --body:"Open Sans",sans-serif;
}
*{box-sizing:border-box;margin:0;padding:0}
html,body{width:1200px;height:2671px;overflow:hidden}
body{position:relative;background:var(--white);font-family:var(--body);color:var(--text)}
.abs{position:absolute}

/* top bar */
.topbar{left:0;top:0;width:1200px;height:32px;background:var(--blue-top);color:var(--white);font-size:12px;font-weight:600}
.topbar .tagline{left:84px;top:8px}
.topbar .call{left:961px;top:8px;display:flex;align-items:center;gap:6px}

/* nav */
.nav{left:0;top:32px;width:1200px;height:107px;background:var(--white)}
.nav a{position:absolute;top:46px;font-family:var(--head);font-weight:600;font-size:15px;color:var(--ink);text-decoration:none;letter-spacing:.3px}
.brand{position:absolute;left:468px;top:34px;width:264px;display:flex;align-items:center;gap:8px}
.brand .dot{width:30px;height:30px;border-radius:50%;background:var(--sky);flex:none}
.brand .name{font-family:var(--head);font-weight:700;font-size:21px;color:var(--ink);white-space:nowrap}

/* hero */
.hero{left:0;top:139px;width:1200px;height:516px;background:radial-gradient(ellipse at 50% 55%,var(--hero-a),var(--hero-b) 75%)}
.hero h1{position:absolute;left:0;width:1200px;text-align:center;font-family:var(--head);font-weight:600;color:var(--white);font-size:46px;line-height:57px;top:54px;text-shadow:0 2px 4px rgba(0,0,0,.4)}
.hero h1 span{margin:0 14px}
.hero-art{left:271px;top:190px;width:637px;height:294px;border-radius:6px;background:linear-gradient(180deg,#c9ccd1,#8d939b 60%,#5a5f68)}

/* services */
.services h2{position:absolute;left:0;top:722px;width:1200px;text-align:center;font-family:var(--head);font-weight:600;font-size:36px;color:var(--ink);letter-spacing:.5px}
.ring{left:386px;top:828px;width:428px;height:428px;border:9px solid var(--ring);border-radius:50%}
.device{left:481px;top:935px;width:210px;height:187px;border-radius:8px;background:linear-gradient(160deg,#3a3d42,#111316)}
.icon-disc{width:124px;height:124px;border-radius:50%;background:var(--sky);border:7px solid var(--ring);display:flex;align-items:center;justify-content:center}
.service-label{font-family:var(--head);font-weight:500;font-size:25px;line-height:32px;color:var(--ink)}
.service-label.right{text-align:right}
.rule{height:1.5px;background:var(--sky)}

/* split */
.split-left{left:0;top:1332px;width:1200px;height:416px;background:var(--sky)}
.split-right{left:0;top:1332px;width:1200px;height:416px}
.split h3{position:absolute;font-family:var(--head);font-weight:600;font-size:34px;color:var(--white);letter-spacing:.5px}
.pill{position:absolute;left:84px;height:57px;border-radius:29px;background:var(--pill);display:flex;align-items:center;padding-left:26px;gap:14px;color:var(--white);font-family:var(--head);font-weight:700;font-size:22px;letter-spacing:.5px}
.avatar{left:605px;top:1479px;width:132px;height:132px;border-radius:50%;border:5px solid var(--sky);background:linear-gradient(180deg,#e9d2c0,#3a8fb8 70%)}
.quote-rule{left:760px;top:1481px;width:1.5px;height:143px;background:#9aa3ad}
.quote{left:785px;top:1482px;width:345px;color:var(--white)}
.quote h4{font-size:14px;font-weight:600;margin-bottom:6px}
.quote p{font-size:11.2px;line-height:18px;font-weight:600}
.quote .by{color:var(--sky);font-size:10.5px;margin-top:8px}
.arrow-btn{top:1643px;width:19px;height:19px;display:flex;align-items:center;justify-content:center}

/* review cta */
.cta{left:0;top:1748px;width:1200px;height:132px;background:var(--light)}
.cta h3{position:absolute;left:91px;top:44px;font-family:var(--head);font-weight:500;font-size:36px;color:var(--ink)}
.cta .btn{position:absolute;left:810px;top:45px;width:264px;height:53px;border-radius:27px;background:var(--blue);color:var(--white);font-family:var(--head);font-weight:600;font-size:22px;display:flex;align-items:center;justify-content:center}

/* blog */
.blog h3{position:absolute;left:91px;top:1930px;font-family:var(--head);font-weight:600;font-size:36px;color:var(--ink)}
.blog-thumb{left:94px;top:2005px;width:210px;height:132px;background:linear-gradient(135deg,#4a3a30,#cfd3d8 55%,#9aa0a8)}
.post{left:320px;top:2003px;width:725px}
.post h4{font-size:15px;font-weight:600;color:var(--blue);text-transform:uppercase}
.post .meta{font-size:10px;color:var(--ink);margin:4px 0 6px}
.post p{font-size:12.2px;line-height:21px;color:var(--ink)}
.post .more{display:block;margin-top:6px;font-size:12px;color:var(--ink)}

/* newsletter */
.newsletter{left:0;top:2204px;width:1200px;height:119px;background:var(--dark)}
.newsletter h3{position:absolute;left:139px;top:38px;font-family:var(--head);font-weight:600;font-size:32px;color:var(--white)}
.field{position:absolute;top:39px;height:37px;background:#f1f1f1;font-size:12px;color:#a0a4aa;padding:12px 8px}
.submit{position:absolute;left:906px;top:39px;width:155px;height:37px;background:#4f8fcb;color:var(--white);font-family:var(--head);font-weight:700;font-size:19px;display:flex;align-items:center;justify-content:center;letter-spacing:.5px}

/* footer */
.footer{left:0;top:2323px;width:1200px;height:348px;background:var(--blue)}
.footer h3{position:absolute;left:123px;top:44px;font-family:var(--head);font-weight:500;font-size:21px;color:var(--white);letter-spacing:.8px}
.map{left:123px;top:111px;width:495px;height:192px;background:linear-gradient(135deg,#eceae4,#dfe3df 60%,#cfdde6)}
.contact-row{position:absolute;left:682px;display:flex;gap:14px;color:var(--white);font-size:15px;line-height:21px}
.contact-row strong{font-weight:700}
.copyright{position:absolute;left:682px;top:280px;color:var(--white);font-size:13px}
</style>
</head>
<body>

<!-- top bar -->
<div class="abs topbar">
  <span class="abs tagline">Looking For A Great New Jersey IT Support Company?</span>
  <span class="abs call">Call:
    <svg width="14" height="14" viewBox="0 0 24 24" fill="#fff"><path d="M6.6 10.8a15 15 0 0 0 6.6 6.6l2.2-2.2c.3-.3.7-.4 1-.2 1.1.4 2.3.6 3.6.6.6 0 1 .4 1 1V20c0 .6-.4 1-1 1A17 17 0 0 1 3 4c0-.6.4-1 1-1h3.5c.6 0 1 .4 1 1 0 1.3.2 2.5.6 3.6.1.3 0 .7-.2 1z"/></svg>
    (973) 555-0148</span>
</div>

<!-- navigation -->
<nav class="abs nav">
  <a style="left:100px">HOME</a>
  <a style="left:185px">ABOUT US</a>
  <a style="left:299px">HOW CAN WE HELP?</a>
  <div class="brand"><span class="dot"></span><span class="name">Brightline Tech Partners</span></div>
  <a style="left:767px">MEDIA</a>
  <a style="left:864px">BLOG</a>
  <a style="left:958px">CONTACT US</a>
</nav>

<!-- hero -->
<section class="abs hero">
  <h1><span>Plan Ahead...</span><span>Work Smarter...</span><span>Stay Strong</span><br>Brightline Tech Partners</h1>
  <div class="abs hero-art" role="img" aria-label="Row of silver server towers with blue trim"></div>
</section>

<!-- services -->
<section class="services">
  <h2>100% US-BASED IT SERVICES &amp; SUPPORT</h2>
  <div class="abs ring"></div>
  <div class="abs device" role="img" aria-label="Black network storage server unit"></div>

  <div class="abs rule" style="left:146px;top:840px;width:226px"></div>
  <div class="abs service-label right" style="left:100px;top:852px;width:200px">Managed IT<br>Services</div>
  <div class="abs icon-disc" style="left:344px;top:855px">
    <svg width="64" height="50" viewBox="0 0 64 50" fill="#1e2a38"><circle cx="20" cy="14" r="9"/><circle cx="44" cy="14" r="9"/><circle cx="32" cy="18" r="10"/><path d="M4 46c0-10 7-17 16-17s12 4 12 4 3-4 12-4 16 7 16 17z"/><path d="M14 50c0-12 8-19 18-19s18 7 18 19z"/></svg>
  </div>

  <div class="abs rule" style="left:801px;top:847px;width:232px"></div>
  <div class="abs service-label" style="left:865px;top:857px">Protect Your<br>Business Data</div>
  <div class="abs icon-disc" style="left:695px;top:851px">
    <svg width="46" height="56" viewBox="0 0 46 56" fill="#1f5f8f"><path d="M10 24V16a13 13 0 0 1 26 0v8h-6v-8a7 7 0 0 0-14 0v8z"/><rect x="4" y="24" width="38" height="30" rx="4"/><circle cx="23" cy="37" r="4" fill="#4f9bd4"/><rect x="21" y="38" width="4" height="9" fill="#4f9bd4"/></svg>
  </div>

  <div class="abs rule" style="left:128px;top:1041px;width:230px"></div>
  <div class="abs service-label right" style="left:64px;top:1076px;width:240px">New Jersey<br>Cloud Computing</div>
  <div class="abs icon-disc" style="left:339px;top:1054px">
    <svg width="76" height="46" viewBox="0 0 76 46" fill="#1e2a38"><path d="M16 44a14 14 0 0 1-2-28 18 18 0 0 1 34-4 14 14 0 0 1 16 12 10 10 0 0 1-2 20z"/></svg>
  </div>

  <div class="abs rule" style="left:805px;top:1056px;width:201px"></div>
  <div class="abs service-label" style="left:863px;top:1073px">Managed Email<br>Solutions</div>
  <div class="abs icon-disc" style="left:712px;top:1054px">
    <svg width="72" height="44" viewBox="0 0 72 44" fill="#1e2a38"><rect x="0" y="10" width="20" height="4"/><rect x="4" y="20" width="16" height="4"/><rect x="8" y="30" width="12" height="4"/><rect x="24" y="4" width="46" height="36" rx="2"/><path d="M26 7l21 18 21-18" stroke="#4f9bd4" stroke-width="3" fill="none"/></svg>
  </div>
</section>

<!-- apart / testimonials -->
<section class="split">
  <div class="abs split-left"></div>
  <svg class="abs split-right" width="1200" height="416" viewBox="0 0 1200 416" role="img" aria-label="Dark blurred office backdrop">
    <defs><linearGradient id="dusk" x1="0" y1="0" x2="0" y2="1"><stop offset="0" stop-color="#4a505a"/><stop offset="1" stop-color="#2e333b"/></linearGradient></defs>
    <polygon points="641,0 1200,0 1200,416 459,416" fill="url(#dusk)"/>
  </svg>
  <h3 style="left:78px;top:1380px">WHAT SETS US APART?</h3>
  <div class="pill" style="top:1453px;width:299px">
    <svg width="24" height="30" viewBox="0 0 24 30" fill="#1e2a38"><circle cx="12" cy="15" r="11"/><circle cx="12" cy="15" r="4" fill="#2f6e9e"/></svg>PLAN AHEAD</div>
  <div class="pill" style="top:1538px;width:272px">
    <svg width="24" height="32" viewBox="0 0 24 32" fill="#1e2a38"><circle cx="12" cy="5" r="4"/><rect x="9" y="10" width="6" height="22"/><rect x="0" y="11" width="24" height="5"/></svg>WORK SMARTER</div>
  <div class="pill" style="top:1623px;width:320px">
    <svg width="26" height="32" viewBox="0 0 26 32" fill="#1e2a38"><circle cx="13" cy="5" r="4"/><path d="M2 10l11 6 11-6v4l-8 5 5 12h-4l-4-9-4 9H5l5-12-8-5z"/></svg>STAY STRONG</div>

  <h3 style="left:644px;top:1381px">TESTIMONIALS</h3>
  <div class="abs avatar" role="img" aria-label="Portrait photo of a smiling client"></div>
  <div class="abs quote-rule"></div>
  <div class="abs quote">
    <h4>Incredible value and peace of mind</h4>
    <p>“Brightline Tech Partners is absolutely the best thing that has happened to me and my computers. In all my years in business I have never found an IT operation that is more responsive, knowledgeable, and service oriented. I have every confidence that Brightline.”</p>
    <p class="by">— Dana Whitcombe, Harborpoint Lending Wayne, NJ</p>
  </div>
  <div class="abs arrow-btn" style="left:1068px;background:var(--sky)"><svg width="8" height="10" viewBox="0 0 8 10"><path d="M6 1L2 5l4 4" stroke="#fff" stroke-width="2" fill="none"/></svg></div>
  <div class="abs arrow-btn" style="left:1093px;background:#9aa0a8"><svg width="8" height="10" viewBox="0 0 8 10"><path d="M2 1l4 4-4 4" stroke="#fff" stroke-width="2" fill="none"/></svg></div>
</section>

<!-- review call to action -->
<section class="abs cta">
  <h3>Book Your Free 2-hour review</h3>
  <div class="btn">Get Started Now!</div>
</section>

<!-- blog -->
<section class="blog">
  <h3>Latest Blog</h3>
  <div class="abs blog-thumb" role="img" aria-label="Close-up of a white keyboard on a wooden desk"></div>
  <div class="abs post">
    <h4>Cloud Security Risks Mostly Come From Employees</h4>
    <div class="meta">06 MAY 2015 By: ADMIN</div>
    <p>You can cancel or close your website and account at any time. To do so, login to Nimbora Hosting with your email/password combination. Your sites will be listed on your dashboard. Click the "delete site" link to delete a website. If you are logging in with a username/password combination.</p>
    <span class="more">Read More</span>
  </div>
</section>

<!-- newsletter -->
<section class="abs newsletter">
  <h3>Newsletters:</h3>
  <div class="field" style="left:372px;width:240px">Name</div>
  <div class="field" style="left:636px;width:238px">Email Address</div>
  <div class="submit">SUBMIT</div>
</section>

<!-- footer -->
<footer class="abs footer">
  <h3>CONTACT YOUR NEW JERSEY IT SUPPORT PROFESSIONALS</h3>
  <div class="abs map" role="img" aria-label="Street map showing the office location in Fairfield, NJ"></div>
  <div class="contact-row" style="top:119px">
    <svg width="20" height="26" viewBox="0 0 20 26" fill="#fff"><path d="M10 0a10 10 0 0 0-10 10c0 7 10 16 10 16s10-9 10-16A10 10 0 0 0 10 0zm0 14a4 4 0 1 1 0-8 4 4 0 0 1 0 8z"/></svg>
    <div><strong>Brightline Tech Partners</strong><br>48 Orchard Lane, Fairfield NJ 07004</div>
  </div>
  <div class="contact-row" style="top:182px">
    <svg width="24" height="24" viewBox="0 0 24 24" fill="none" stroke="#fff" stroke-width="2"><circle cx="12" cy="12" r="10"/><path d="M8.5 7.5l2 2-1 1.5a8 8 0 0 0 3.5 3.5l1.5-1 2 2-1.5 1.5c-3 0-8-5-8-8z" fill="#fff" stroke="none"/></svg>
    <div>+1 973-555-0192</div>
  </div>
  <div class="contact-row" style="top:230px">
    <svg width="22" height="18" viewBox="0 0 22 18" fill="#fff"><rect x="0" y="2" width="22" height="15" rx="1"/><path d="M1 3l10 8 10-8" stroke="#2b76b0" stroke-width="2" fill="none"/></svg>
    <div>hello@brightlinetech.example</div>
  </div>
  <div class="copyright">Copyright © 2016. Brightline Tech Partners. All Right Revered</div>
</footer>

</body>
</html>
```